Pantry Circle is an online food market place that connects foodies who make or grow great food with

We would like a 1/2 A4 page size flyer in landscape to promote our new business. We would like to encourage new home foodies to sign up for a membership on our website www.pantrycirclenz.co.nz and we would like customers who are looking for great food in their local community to search our website for their closest home foodie and support a neighbour who is growing or producing creative food locally

Target Market(s)

Creative food lovers

Industry/Entity Type

Landscape

Colors
acd037
f78f20
33b8a4

Requirements
Must have
• Food images and look groovy
• Must be easy to read and stand out on a notice board
• Website address www.pantrycirclenz.co.nz
Nice to have
• We wish to use this flyer in multiple locations and wish to put in different contact details prior to printing

```html
<!DOCTYPE html>
<html lang="en">
<head>
<meta charset="utf-8">
<title>Pantry Circle Flyer</title>
<link rel="stylesheet" href="https://fonts.googleapis.com/css2?family=PT+Sans:wght@400;700&family=PT+Sans+Narrow:wght@700&display=swap">
<style>
  :root {
    --backdrop: #a4a4a4;
    --wood-light: #b7ab9e;
    --wood-mid: #9c8b7a;
    --wood-dark: #7d6a5a;
    --cloth: #7fd0d6;
    --spoon: #a65a2c;
    --brand-green: #80b83f;
    --headline-green: #8cc63f;
    --brown: #4a3426;
    --panel-white: rgba(255, 255, 255, 0.62);
    --ink: #111111;
    --white: #ffffff;
  }
  * { margin: 0; padding: 0; box-sizing: border-box; }
  html, body {
    width: 1200px;
    height: 911px;
    overflow: hidden;
    background: var(--backdrop);
  }
  .canvas {
    position: relative;
    width: 1200px;
    height: 911px;
  }
  .flyer {
    position: absolute;
    left: 117px;
    top: 114px;
    width: 966px;
    height: 683px;
    overflow: hidden;
    font-family: "PT Sans", sans-serif;
  }
  .flyer-photo {
    position: absolute;
    inset: 0;
    background:
      radial-gradient(ellipse 260px 380px at 190px 330px, rgba(166, 90, 44, 0.55), transparent 70%),
      radial-gradient(ellipse 330px 520px at 230px 460px, rgba(127, 208, 214, 0.75), transparent 72%),
      linear-gradient(180deg, var(--wood-mid) 0%, var(--wood-light) 40%, var(--wood-mid) 75%, var(--wood-dark) 100%);
  }
  .brand-panel {
    position: absolute;
    left: 540px;
    top: 0;
    width: 276px;
    height: 256px;
    background: var(--panel-white);
    display: flex;
    flex-direction: column;
    align-items: center;
    justify-content: center;
    gap: 14px;
  }
  .brand-mark {
    width: 56px;
    height: 56px;
    border-radius: 50%;
    background: var(--brand-green);
  }
  .brand-name {
    font-family: "PT Sans Narrow", sans-serif;
    font-weight: 700;
    font-size: 44px;
    line-height: 1;
    color: var(--brown);
    text-transform: uppercase;
    text-align: center;
  }
  .headline {
    position: absolute;
    left: 420px;
    top: 302px;
    width: 518px;
    text-align: center;
    font-family: "PT Sans Narrow", sans-serif;
    font-weight: 700;
    font-size: 29px;
    line-height: 38px;
    letter-spacing: -0.3px;
    color: var(--headline-green);
    -webkit-text-stroke: 0.6px var(--white);
    text-shadow:
      -1px -1px 0 var(--white), 1px -1px 0 var(--white),
      -1px 1px 0 var(--white), 1px 1px 0 var(--white),
      3px 3px 3px rgba(40, 30, 20, 0.75);
  }
  .info-box {
    position: absolute;
    left: 0;
    top: 489px;
    width: 361px;
    height: 162px;
    background: var(--brand-green);
    color: var(--white);
    text-align: center;
    padding-top: 56px;
  }
  .info-label {
    font-size: 17px;
    line-height: 22px;
  }
  .info-url {
    font-weight: 700;
    font-size: 24px;
    line-height: 30px;
    letter-spacing: -0.2px;
  }
  .benefits-panel {
    position: absolute;
    left: 383px;
    top: 489px;
    width: 583px;
    height: 162px;
    background: var(--panel-white);
    padding: 33px 20px 0 31px;
    color: var(--ink);
    font-size: 15px;
    line-height: 18px;
  }
  .benefit + .benefit { margin-top: 17px; }
</style>
</head>
<body>
<div class="canvas">
  <section class="flyer">
    <div class="flyer-photo" role="img" aria-label="Wooden spoon and salad fork tied with raffia resting on a turquoise gingham napkin over weathered wooden boards"></div>

    <div class="brand-panel">
      <div class="brand-mark"></div>
      <div class="brand-name">Pantry Circle</div>
    </div>

    <h1 class="headline">Be part of our exciting new<br>online food marketplace connecting<br>foodies in your local community</h1>

    <div class="info-box">
      <p class="info-label">For more information go to:</p>
      <p class="info-url">www.pantrycirclenz.co.nz</p>
    </div>

    <div class="benefits-panel">
      <p class="benefit"># As a foodie you can sell your beautiful home produced or home grown produce on our marketplace website</p>
      <p class="benefit"># As a food lover you can purchase lovingly grown or prepared food and support your local foodie community while keeping your food miles low</p>
    </div>
  </section>
</div>
</body>
</html>
```